Business Cards and Logo needed for Rum Website

I need a smart, modern but fun business card (and Logo) to help promote my website BrightBarrelNote.com

The website contains reviews of Rum (and eventually other spirits) as well as news and blog posts.

I would like a 2-sided design, with the logo and company name on one side and text on the other.

Text fields required are:
Name (Dan Wheeler)
Website (www.brightbarrelnote.com)
Email (dan@brightbarrelnote.com)
Twitter (@BrightBarrelNote)

For the logo i'm open to suggestions however it must incorporate a wooden Cask and a number of Stars. Ideas so far have been for a Cask surrounded in a number of Stars forming a circle around it with the text Bright Barrel Note underneath. The logo should be modern but also a little bit cartoony and stylised. General drink/spirits themes will also be considered.

Colours: I like the idea of yellow text with black background but again i'm open to suggestions on what would work well. Contrasting colours for the 2-sides would be good.

Cards will be printed via Printlo.com so please consult their style guidelines if required: http://uk.printlo.com/help/faq/templates-and-guidelines.html

Requirements
Must have
• A spirits Cask
A number of Stars (preferrably yellow or gold)

```html
<!DOCTYPE html>
<html lang="en">
<head>
<meta charset="utf-8">
<title>Bright Barrel Note – Business Card</title>
<link rel="stylesheet" href="https://fonts.googleapis.com/css2?family=Indie+Flower&display=swap">
<style>
  :root {
    --page: #ffffff;
    --card-dark: #0a0a0a;
    --card-bright: #dfdf00;
    --ink-light: #ffffff;
    --ink-dark: #111111;
    --accent: #e6e200;
  }
  html, body {
    margin: 0;
    padding: 0;
    width: 1200px;
    height: 900px;
    overflow: hidden;
    background: var(--page);
  }
  .canvas {
    position: relative;
    width: 1200px;
    height: 900px;
    font-family: "Indie Flower", cursive;
  }
  .card {
    position: absolute;
    box-sizing: border-box;
  }
  .card--front {
    left: 169px;
    top: 91px;
    width: 382px;
    height: 624px;
    background: var(--card-dark);
  }
  .card--back {
    left: 688px;
    top: 184px;
    width: 380px;
    height: 622px;
    background: var(--card-bright);
  }
  .brand {
    position: absolute;
    left: 0;
    top: 60px;
    width: 100%;
    text-align: center;
    color: var(--ink-light);
    font-size: 46px;
    line-height: 1.05;
  }
  .brand-dot {
    position: absolute;
    left: 290px;
    top: 36px;
    width: 18px;
    height: 18px;
    border-radius: 50%;
    background: var(--accent);
  }
  .balloon-string {
    position: absolute;
    left: 0;
    top: 0;
  }
  .tld {
    position: absolute;
    left: 142px;
    top: 458px;
    color: var(--accent);
    font-size: 26px;
    line-height: 1;
  }
  .front-url {
    position: absolute;
    left: 0;
    width: 100%;
    top: 548px;
    text-align: center;
    color: var(--ink-light);
    font-size: 30px;
    line-height: 1;
  }
  .contact {
    position: absolute;
    left: 80px;
    top: 416px;
    margin: 0;
    padding: 0;
    list-style: none;
    color: var(--ink-dark);
  }
  .contact li {
    font-size: 26px;
    line-height: 46px;
    white-space: nowrap;
  }
  .contact .contact-name {
    font-weight: 700;
    line-height: 40px;
  }
</style>
</head>
<body>
<main class="canvas">
  <section class="card card--front" aria-label="Card front">
    <div class="brand-dot"></div>
    <div class="brand">Bright Barrel<br>Note</div>
    <svg class="balloon-string" width="382" height="624" viewBox="0 0 382 624" aria-hidden="true">
      <path d="M76 214 C46 270, 46 410, 136 480" fill="none" stroke="#ffffff" stroke-width="3" stroke-dasharray="3 5" stroke-linecap="round"/>
    </svg>
    <div class="tld">com</div>
    <div class="front-url">BrightBarrelNote.com</div>
  </section>

  <section class="card card--back" aria-label="Card back">
    <ul class="contact">
      <li class="contact-name">Dan Wheeler</li>
      <li>www.brightbarrelnote.com</li>
      <li>dan@brightbarrelnote.com</li>
      <li>Twitter (@BrightBarrelNote)</li>
    </ul>
  </section>
</main>
</body>
</html>
```